Registry Program Flyer Design 1 - LPLD registry

We need two different flyers that will be distributed via web, email and print. This project is for one of the two flyers.

The audience is patients and family members of patients with a specific disease. The flyer will be used to make patients aware of our web-based registry programs, and to inform/encourage patients to join.

An example prototype flyer with the text that should be used is attached. We would like to improve the design and layout of the flyers, while retaining as much of the language as appropriate.

For this project, the flyer may use the pictures included in the prototype, however, it is not required.

If possible, a final format that allows us to edit the text is preferred. If this is not possible, we will finalize the text after receiving a prototype. Changes to the text will likely be minor.

Note: The design of the flyers for this project and the other project (Registry Program Flyer design 2 - TQ Harbor registry) can be similar in style, however, they should not be duplicates.

Final deliverable should be in a .PSD format (photoshop) with layers so we can edit text if necessary.

Physicians and healthcare providers

• Use the attached logo file and color scheme.

```html
<!DOCTYPE html>
<html lang="en">
<head>
<meta charset="utf-8">
<title>TQ Harbor – LPLD Registry Flyer</title>
<link rel="stylesheet" href="https://fonts.googleapis.com/css2?family=Open+Sans:wght@300;400;600;700;800&display=swap">
<style>
  :root {
    --brand-blue: #2f6fb7;
    --brand-deep: #22558f;
    --logo-blue: #3d7cc4;
    --tint: #eaf1f9;
    --rule: #c9d9ec;
    --paper: #ffffff;
    --ink: #1f2933;
    --muted: #44515e;
    --photo-doctor: linear-gradient(135deg, #dfe6ee 0%, #b9c7d6 55%, #8fa4bb 100%);
    --photo-elder: linear-gradient(135deg, #c9b9a6 0%, #e6d9c8 50%, #9fb0c0 100%);
    --photo-carer: linear-gradient(135deg, #e8dccd 0%, #c6b3a0 55%, #8aa3c2 100%);
  }
  * { box-sizing: border-box; margin: 0; padding: 0; }
  html, body { width: 844px; height: 1200px; overflow: hidden; }
  body { background: var(--paper); font-family: "Open Sans", Arial, sans-serif; color: var(--ink); }
  .flyer { width: 844px; height: 1200px; display: grid; grid-template-rows: 96px 224px 72px 808px; }

  /* Header */
  .masthead { display: flex; align-items: center; border-top: 8px solid var(--brand-blue); }
  .brand { width: 250px; display: flex; align-items: center; gap: 12px; padding-left: 34px; }
  .brand-dot { width: 30px; height: 30px; border-radius: 50%; background: var(--logo-blue); flex: none; }
  .brand-name { font-size: 24px; font-weight: 600; color: var(--logo-blue); white-space: nowrap; }
  .tagline { flex: 1; border-left: 3px solid var(--brand-blue); padding: 0 24px 0 20px; font-size: 19px; line-height: 1.35; font-weight: 400; color: var(--brand-deep); }

  /* Photo strip */
  .photo-strip { display: grid; grid-template-columns: 1fr 1.15fr 1fr; gap: 6px; }
  .photo-doctor { background: var(--photo-doctor); }
  .photo-elder { background: var(--photo-elder); }
  .photo-carer { background: var(--photo-carer); }

  /* Join bar */
  .join-bar { background: var(--brand-blue); color: var(--paper); display: flex; align-items: center; justify-content: center; gap: 18px; }
  .join-label { font-size: 30px; font-weight: 300; }
  .join-url { font-size: 32px; font-weight: 800; letter-spacing: 0.2px; }

  /* Body */
  .content { display: grid; grid-template-columns: 540px 304px; }
  .main { padding: 26px 30px 24px 36px; display: flex; flex-direction: column; }
  .main h2 { font-size: 24px; font-weight: 700; color: var(--brand-blue); margin-bottom: 12px; }
  .main p { font-size: 15.5px; line-height: 1.45; color: var(--ink); margin-bottom: 14px; }
  .main .lead-in { font-weight: 600; margin-bottom: 8px; }
  .benefits { list-style: none; margin-bottom: 16px; }
  .benefits li { display: flex; gap: 10px; font-size: 15.5px; line-height: 1.4; margin-bottom: 6px; }
  .benefits svg { flex: none; width: 18px; height: 18px; margin-top: 2px; }
  .encourage { font-weight: 600; color: var(--brand-deep); }

  .cta-card { margin-top: auto; background: var(--brand-blue); color: var(--paper); padding: 18px 24px 16px; }
  .cta-line { font-size: 19px; font-weight: 700; }
  .cta-strong { font-size: 27px; font-weight: 800; line-height: 1.2; }
  .cta-contact { margin-top: 12px; padding-top: 10px; border-top: 1px solid rgba(255,255,255,0.45); display: flex; justify-content: space-between; align-items: flex-end; font-size: 13.5px; line-height: 1.4; }
  .cta-contact strong { font-weight: 700; }
  .copyright { font-size: 11.5px; text-align: right; opacity: 0.9; }

  .sidebar { background: var(--tint); padding: 24px 24px 20px 24px; border-left: 1px solid var(--rule); }
  .sidebar section + section { margin-top: 16px; padding-top: 14px; border-top: 1px solid var(--rule); }
  .sidebar h3 { font-size: 17px; font-weight: 700; color: var(--brand-blue); margin-bottom: 8px; }
  .audience { list-style: none; font-size: 14px; line-height: 1.45; }
  .audience li { position: relative; padding-left: 14px; }
  .audience li::before { content: ""; position: absolute; left: 0; top: 8px; width: 6px; height: 6px; border-radius: 50%; background: var(--brand-blue); }
  .sidebar p { font-size: 12.5px; line-height: 1.45; color: var(--muted); }
  .sidebar p + p { margin-top: 8px; }
</style>
</head>
<body>
<div class="flyer">
  <header class="masthead">
    <div class="brand">
      <span class="brand-dot"></span>
      <span class="brand-name">TQ Harbor</span>
    </div>
    <p class="tagline">Connecting patients, healthcare professionals, researchers &amp; policy makers</p>
  </header>

  <div class="photo-strip">
    <div class="photo-doctor" role="img" aria-label="Smiling doctor in a white coat with a colleague behind him"></div>
    <div class="photo-elder" role="img" aria-label="Smiling older man with a supportive hand on his shoulder"></div>
    <div class="photo-carer" role="img" aria-label="Young caregiver smiling with an older woman"></div>
  </div>

  <div class="join-bar">
    <span class="join-label">Join</span>
    <span class="join-url">www.TQHarborRegistry.org</span>
  </div>

  <div class="content">
    <main class="main">
      <h2>Get Connected.</h2>
      <p>It takes whole communities to help people living with medical conditions lead healthier and happier lives.. The HARBOR LPLD Registry brings together individuals affected by lipoprotein lipase deficiency and professionals involved in their medical care and research.</p>
      <p class="lead-in">Join THE HARBOR LPLD Registry to:</p>
      <ul class="benefits">
        <li><svg viewBox="0 0 18 18" aria-hidden="true"><circle cx="9" cy="9" r="9" fill="#2f6fb7"/><path d="M5 9.3l2.6 2.6L13 6.5" fill="none" stroke="#fff" stroke-width="2" stroke-linecap="round" stroke-linejoin="round"/></svg><span>Learn how other patients manage their health</span></li>
        <li><svg viewBox="0 0 18 18" aria-hidden="true"><circle cx="9" cy="9" r="9" fill="#2f6fb7"/><path d="M5 9.3l2.6 2.6L13 6.5" fill="none" stroke="#fff" stroke-width="2" stroke-linecap="round" stroke-linejoin="round"/></svg><span>Take surveys and share your experiences in a program that safeguards your privacy</span></li>
        <li><svg viewBox="0 0 18 18" aria-hidden="true"><circle cx="9" cy="9" r="9" fill="#2f6fb7"/><path d="M5 9.3l2.6 2.6L13 6.5" fill="none" stroke="#fff" stroke-width="2" stroke-linecap="round" stroke-linejoin="round"/></svg><span>Receive information about opportunities to participate in research</span></li>
        <li><svg viewBox="0 0 18 18" aria-hidden="true"><circle cx="9" cy="9" r="9" fill="#2f6fb7"/><path d="M5 9.3l2.6 2.6L13 6.5" fill="none" stroke="#fff" stroke-width="2" stroke-linecap="round" stroke-linejoin="round"/></svg><span>Help researchers unlock more effective treatments</span></li>
        <li><svg viewBox="0 0 18 18" aria-hidden="true"><circle cx="9" cy="9" r="9" fill="#2f6fb7"/><path d="M5 9.3l2.6 2.6L13 6.5" fill="none" stroke="#fff" stroke-width="2" stroke-linecap="round" stroke-linejoin="round"/></svg><span>Help healthcare providers better understand LPLD</span></li>
        <li><svg viewBox="0 0 18 18" aria-hidden="true"><circle cx="9" cy="9" r="9" fill="#2f6fb7"/><path d="M5 9.3l2.6 2.6L13 6.5" fill="none" stroke="#fff" stroke-width="2" stroke-linecap="round" stroke-linejoin="round"/></svg><span>Improve knowledge about patient communities among advocacy groups</span></li>
      </ul>
      <p>The more data we collect about an illness, the closer we can get to helping communities find treatments that work. Your participation is crucial to help reach the goal of developing more effective treatments for LPLD.</p>
      <p class="encourage">Encourage everyone you know to join today!</p>

      <div class="cta-card">
        <div class="cta-line">Learn from others... Make a difference....</div>
        <div class="cta-strong">Get Connected</div>
        <div class="cta-contact">
          <div><strong>www.TQHarborRegistry.org</strong><br>info@carebridgenet.com</div>
          <div class="copyright">Copyright © 2014<br>CareBridge Network</div>
        </div>
      </div>
    </main>

    <aside class="sidebar">
      <section>
        <h3>Who Can Benefit</h3>
        <ul class="audience">
          <li>Patients</li>
          <li>Healthcare providers</li>
          <li>Researchers</li>
          <li>Industry representatives</li>
          <li>Policy-makers</li>
          <li>All stakeholders interested in LPLD</li>
        </ul>
      </section>
      <section>
        <h3>How it Works</h3>
        <p>Patients can join the registry to submit their data. After taking web-based surveys, explore the collected information in a way that protects the privacy of everyone.</p>
      </section>
      <section>
        <h3>Who We Are</h3>
        <p>The Lipid Care Alliance Foundation (LCAF) reviewed the registry survey. As a professional organization, our mission has been to reduce the morbidity and mortality from cardiovascular disease by increasing the understanding of the pathophysiology, and detection and optimal treatment of lipid disorders.</p>
        <p>CareBridge Network pioneered the HARBOR registry platform, which allows patients around the world to join others in reporting their own experience of disease. In use since 2007, our registries collect data from patients for over 350 diseases worldwide for foundations, companies and governments.</p>
      </section>
    </aside>
  </div>
</div>
</body>
</html>
```